Social Movement/Church Plant Website - KindAshbury.com

We need a website for our church plant startup, however we want the focus of the landing page to be around #kindashbury - that we are an organization that is FOR our town (Ashbury). The site will include serving project events, social events, a place to sign up for emails, a blog, a place to give, etc. All the elements we know we want are currently at kindashbury.com . Please check this for copy.

We want this to be easy to edit as a non-developer.

I have included several logos with our colors, as well as an ai file to give you an idea of how we want the design to look and feel - also includes our branded fonts

Target Market(s)

People who live in the Northern CO area

Font styles to use
Serif
Sans Serif

Requirements
Must have
• Events (serve and social), Blog section, A place to get involved - where to give and to sign up for emails. Must match our branding colors and style hex 4c7991.
Should not have
• Should not be focused on the actual church plant on the home page. There can be some back end stuff about it, but the focus should be #kindashbury.

```html
<!DOCTYPE html>
<html lang="en">
<head>
<meta charset="utf-8">
<title>KindAshbury.com</title>
<link rel="stylesheet" href="https://fonts.googleapis.com/css2?family=Montserrat:wght@400;600;700&family=Open+Sans:wght@400;600;700&display=swap">
<style>
:root{
  --brand:#4c7991;
  --brand-dark:#3d6479;
  --orange:#f15a24;
  --yellow:#f6b21b;
  --ink:#333;
  --muted:#777;
  --light:#f3f4f5;
  --dark:#2b2b2b;
  --white:#fff;
}
*{box-sizing:border-box;margin:0;padding:0}
html,body{width:1200px;height:3648px;overflow:hidden}
body{font-family:"Open Sans",Arial,sans-serif;color:var(--ink);background:var(--white);position:relative}
h1,h2,h3,h4,.btn,.nav a{font-family:"Montserrat",Arial,sans-serif}
.abs{position:absolute}
.ph{position:absolute;display:block}
.btn{display:inline-block;color:var(--white);font-weight:700;font-size:13px;letter-spacing:1px;text-transform:uppercase;padding:12px 24px;text-decoration:none}
.btn-orange{background:var(--orange)}
.btn-brand{background:var(--brand)}
.section-title{font-size:20px;font-weight:700;letter-spacing:1px;text-align:center;text-transform:uppercase;color:var(--ink)}

/* header */
.site-header{position:absolute;top:0;left:0;width:1200px;height:124px;background:var(--white)}
.logo{position:absolute;left:132px;top:30px;display:flex;align-items:center;gap:10px}
.logo-mark{width:40px;height:40px;background:var(--brand)}
.logo-name{font-family:"Montserrat",sans-serif;font-weight:700;font-size:22px;color:var(--brand)}
.header-actions{position:absolute;right:300px;top:28px;display:flex;gap:8px}
.header-actions .btn{font-size:11px;padding:8px 14px;line-height:1.1;text-align:center}
.header-actions small{display:block;font-size:8px;font-weight:400;letter-spacing:0}
.social{display:flex;gap:6px}
.social span{display:block;width:22px;height:22px}
.header-social{position:absolute;left:940px;top:34px}
.nav{position:absolute;left:132px;top:92px;width:936px;height:32px;border-top:1px solid #e4e4e4;display:flex;gap:26px;align-items:center}
.nav a{font-size:11px;font-weight:700;color:var(--ink);text-decoration:none;letter-spacing:.5px}

/* hero */
.hero{position:absolute;top:124px;left:0;width:1200px;height:448px;overflow:hidden}
.hero-photo{inset:0;background:linear-gradient(120deg,#6c5444 0%,#a47f63 35%,#c89c78 55%,#7c6452 80%,#4d3c33 100%)}
.hero-shade{position:absolute;inset:0;background:linear-gradient(90deg,rgba(20,25,30,.55),rgba(20,25,30,.15))}
.hero-copy{position:absolute;left:168px;top:118px;width:460px;color:var(--white)}
.hero-copy h1{font-size:27px;line-height:1.28;font-weight:700;text-transform:uppercase}
.hero-copy p{font-size:12px;line-height:1.6;margin:14px 0 22px;opacity:.9}
.hero-arrow{position:absolute;top:200px;width:36px;height:46px;background:rgba(255,255,255,.25)}
.hero-arrow svg{display:block;margin:13px auto}

/* story */
.story{position:absolute;top:572px;left:0;width:1200px;height:428px;background:var(--light)}
.story-body{position:absolute;left:300px;top:84px;width:600px;text-align:center}
.story-body h4{font-size:12px;color:var(--muted);font-weight:600;margin:6px 0 18px}
.story-body p{font-size:11.5px;line-height:1.75;color:var(--muted);margin-bottom:12px}
.diamond{position:absolute;transform:rotate(45deg);border:4px solid var(--white)}

/* events */
.events{position:absolute;top:1000px;left:0;width:1200px;height:480px;background:var(--white)}
.events .section-title{position:absolute;top:66px;width:100%}
.event-card{position:absolute;top:126px;width:296px}
.event-card .ph{position:relative;height:162px}
.date-badge{position:absolute;top:0;right:12px;width:46px;height:52px;background:var(--orange);color:var(--white);text-align:center;font-family:"Montserrat",sans-serif;font-weight:700;font-size:17px;padding-top:8px;line-height:1.1}
.date-badge small{display:block;font-size:10px;font-weight:600}
.event-card h3{font-size:13px;font-weight:700;margin:12px 0 6px}
.event-card p{font-size:10.5px;line-height:1.55;color:var(--muted)}
.dots{position:absolute;top:1436px;left:572px;display:flex;gap:10px}
.dots span{width:8px;height:8px;border-radius:50%;background:#c9c9c9}
.dots span:first-child{background:var(--brand)}

/* partner */
.partner{position:absolute;top:1470px;left:0;width:1200px;height:340px}
.partner-bg{position:absolute;inset:0}
.partner-copy{position:absolute;top:124px;width:100%;text-align:center;color:var(--white)}
.partner-copy h2{font-size:19px;font-weight:700;text-transform:uppercase;letter-spacing:.5px}
.partner-copy p{font-family:"Montserrat",sans-serif;font-style:normal;font-size:14px;margin-top:10px;opacity:.9}
.partner-actions{position:absolute;top:222px;left:180px;display:flex;gap:8px}
.partner-actions .btn{width:264px;height:56px;display:flex;align-items:center;justify-content:center;gap:12px;font-size:13px}
.btn-blue{background:#2e8ad8}
.btn-yellow{background:var(--yellow)}
.icon-dot{width:18px;height:18px;border:2px solid var(--white);border-radius:50%}

/* blog */
.blog{position:absolute;top:1810px;left:0;width:1200px;height:520px;background:var(--white)}
.blog .section-title{position:absolute;top:116px;width:100%}
.post-row{position:absolute;left:132px;width:460px;display:flex;gap:16px;align-items:flex-start}
.post-row .ph{position:relative;flex:0 0 106px;height:96px}
.post-text{flex:1 1 auto;min-width:0}
.post-row h3{font-size:12px;font-weight:700;margin:4px 0 6px;line-height:1.35}
.post-row p{font-size:10px;line-height:1.55;color:var(--muted)}
.post-row .mini-date{flex:0 0 32px;height:38px;margin-top:4px;background:var(--orange);color:var(--white);font-size:12px;font-weight:700;text-align:center;padding-top:4px;line-height:1.1;font-family:"Montserrat",sans-serif}
.post-row .mini-date small{display:block;font-size:8px}
.feature{position:absolute;left:620px;top:178px;width:448px}
.feature .ph{position:relative;height:234px}
.feature .date-badge{top:auto;bottom:-20px;right:12px;width:58px;height:60px;font-size:20px}
.feature h3{font-size:13px;font-weight:700;margin:14px 0 6px}
.feature p{font-size:10.5px;line-height:1.55;color:var(--muted);width:370px}

/* testimonials */
.testimonials{position:absolute;top:2330px;left:0;width:1200px;height:482px}
.testimonials .section-title{position:absolute;top:190px;width:100%;color:var(--white)}
.quote{position:absolute;top:270px;width:276px;height:164px;background:rgba(255,255,255,.16);padding:44px 22px 0;text-align:center;color:var(--white)}
.quote p{font-size:10.5px;line-height:1.6}
.quote h4{font-size:10px;font-weight:700;margin-top:12px}
.avatar{position:absolute;top:-30px;left:108px;width:60px;height:60px;border-radius:50%;border:3px solid var(--white);background:linear-gradient(#7a6a5e,#b59a82)}
.t-arrow{position:absolute;top:318px;width:28px;height:28px;border-radius:50%;background:rgba(255,255,255,.35)}
.t-arrow svg{display:block;margin:8px auto}

/* newsletter */
.newsletter{position:absolute;top:2812px;left:0;width:1200px;height:88px;background:var(--orange)}
.newsletter p{position:absolute;left:168px;top:34px;color:var(--white);font-size:14px;font-weight:600}
.field{background:var(--white);border:none;font-size:11px;color:#999;padding:0 12px;display:flex;align-items:center}
.newsletter .field{position:absolute;top:30px;width:200px;height:30px}
.newsletter .btn{position:absolute;left:918px;top:30px;height:30px;padding:0 18px;line-height:30px;background:var(--yellow);font-size:11px}

/* follow */
.follow{position:absolute;top:2900px;left:0;width:1200px;height:80px;background:var(--white);text-align:center}
.follow h2{font-size:16px;font-weight:700;padding-top:16px}
.follow .social{justify-content:center;margin-top:12px}
.photo-strip{position:absolute;top:2980px;left:0;width:1200px;height:140px;display:flex}
.photo-strip .ph{position:relative;flex:1}

/* contact */
.contact{position:absolute;top:3120px;left:0;width:1200px;height:500px;background:var(--dark)}
.contact h2{position:absolute;top:52px;width:100%;text-align:center;color:var(--white);font-size:16px;font-weight:700}
.contact .field{position:absolute;height:40px}
.contact .message{align-items:flex-start;padding-top:12px}
.contact .btn{position:absolute;left:548px;top:400px;padding:12px 30px;font-size:11px}
.site-footer{position:absolute;top:3620px;left:0;width:1200px;height:28px;background:#1f1f1f;color:#8a8a8a;font-size:10px;text-align:center;line-height:28px}
</style>
</head>
<body>

<header class="site-header">
  <div class="logo"><span class="logo-mark"></span><span class="logo-name">KindAshbury</span></div>
  <div class="header-actions">
    <a class="btn btn-orange"><small>Make a</small>Donation</a>
    <a class="btn btn-orange"><small>Become a</small>Volunteer</a>
  </div>
  <div class="social header-social">
    <span style="background:#3b5998"></span><span style="background:#29a9e0"></span><span style="background:#c13584"></span><span style="background:#d93a2b"></span><span style="background:#cb2027"></span>
  </div>
  <nav class="nav">
    <a>HOME</a><a>ABOUT US</a><a>VIDEOS</a><a>EVENTS</a><a>BLOG</a><a>GIVE</a><a>CONTACT</a>
  </nav>
</header>

<section class="hero">
  <div class="ph hero-photo" role="img" aria-label="Photo of neighbours sharing a meal around a table"></div>
  <div class="hero-shade"></div>
  <div class="hero-arrow" style="left:0"><svg width="10" height="18"><path d="M9 1L1 9l8 8" stroke="#fff" stroke-width="2" fill="none"/></svg></div>
  <div class="hero-arrow" style="right:0"><svg width="10" height="18"><path d="M1 1l8 8-8 8" stroke="#fff" stroke-width="2" fill="none"/></svg></div>
  <div class="hero-copy">
    <h1>A movement to restore hope, strength, and purpose through the gospel of Jesus.</h1>
    <p>We are neighbours who love our town and want to serve it well, together, every single week of the year.</p>
    <a class="btn btn-orange">Learn More</a>
  </div>
</section>

<section class="story">
  <div class="diamond ph" role="img" aria-label="Photo of volunteers outdoors" style="left:-30px;top:30px;width:100px;height:100px;background:linear-gradient(#8ca5b3,#5d7d8e)"></div>
  <div class="diamond ph" role="img" aria-label="Photo of friends smiling together" style="left:52px;top:100px;width:110px;height:110px;background:linear-gradient(#b69a7f,#6d8a6e)"></div>
  <div class="diamond ph" role="img" aria-label="Photo of a group at a park" style="left:-20px;top:190px;width:120px;height:120px;background:linear-gradient(#7f9e74,#4d6b52)"></div>
  <div class="diamond ph" role="img" aria-label="Photo of a community service day" style="left:110px;top:210px;width:80px;height:80px;background:linear-gradient(#c7a98b,#8b6f59)"></div>
  <div class="diamond ph" role="img" aria-label="Photo of a child at the pool" style="left:1080px;top:60px;width:110px;height:110px;background:linear-gradient(#5fa8c8,#2f6f8f)"></div>
  <div class="diamond ph" role="img" aria-label="Photo of a family event" style="left:1010px;top:150px;width:90px;height:90px;background:linear-gradient(#b4a07e,#7d6a4c)"></div>
  <div class="diamond ph" role="img" aria-label="Photo of a festival with balloons" style="left:1110px;top:200px;width:100px;height:100px;background:linear-gradient(#d96b6b,#7a9ad0)"></div>
  <div class="story-body">
    <h2 class="section-title">Our Story</h2>
    <h4>Working Toward a Better Tomorrow</h4>
    <p>We're a small team of neighbours who believe good things happen when people show up for one another. Every month we plan serve days, shared meals and simple ways to help the families, schools and local groups that make Ashbury feel like home.</p>
    <p>We are for the whole community and we want to be known by how we love our neighbours. Whether you join us for a cleanup, a cookout or a quiet coffee, there is room for you here. Come as you are and bring a friend along.</p>
    <a class="btn btn-brand" style="margin-top:10px;font-size:11px;padding:10px 22px">Contact Us</a>
  </div>
</section>

<section class="events">
  <h2 class="section-title">Upcoming Events</h2>
  <article class="event-card" style="left:132px">
    <div class="ph" role="img" aria-label="Photo of a child swimming at an outdoor pool" style="background:linear-gradient(#58b3d6,#2f7fa6)"><div class="date-badge">18<small>JUN</small></div></div>
    <h3>Riverside Outdoor Pool</h3>
    <p>June 18 · 1:00 PM · Riverside Outdoor Pool, 120 Park St. Ashbury. Bring a towel and snacks for a fun family swim day.</p>
  </article>
  <article class="event-card" style="left:452px">
    <div class="ph" role="img" aria-label="Photo of a school building" style="background:linear-gradient(#9fb3bf,#6e8796)"><div class="date-badge">21<small>JUN</small></div></div>
    <h3>School Cleanup</h3>
    <p>June 21 · 9:00 AM · Help us tidy classrooms and grounds before the new school year begins.</p>
  </article>
  <article class="event-card" style="left:772px">
    <div class="ph" role="img" aria-label="Photo of volunteers packing supplies outdoors" style="background:linear-gradient(#9db08a,#6b7d5c)"><div class="date-badge">25<small>JUN</small></div></div>
    <h3>Building Supply Kits for Local School</h3>
    <p>June 25 · 10:00 AM · Community Hall, 45 Oak Ave. Ashbury. Pack backpacks with school supplies for local kids.</p>
  </article>
</section>
<div class="dots"><span></span><span></span><span></span></div>

<section class="partner">
  <svg class="partner-bg" width="1200" height="340" viewBox="0 0 1200 340" preserveAspectRatio="none" role="img" aria-label="Faded photo of volunteers working together, tinted blue">
    <path d="M0 40 C300 0 500 70 800 40 C1000 20 1120 30 1200 10 L1200 300 C900 340 700 280 400 310 C200 330 80 300 0 320 Z" fill="#4c7991"/>
    <path d="M0 40 C300 0 500 70 800 40 C1000 20 1120 30 1200 10 L1200 40 C900 70 500 20 0 70 Z" fill="#6f97ad" opacity=".6"/>
  </svg>
  <div class="partner-copy">
    <h2>Interested in Partnering With Us?</h2>
    <p>We would love to partner with you to help in our community!</p>
  </div>
  <div class="partner-actions">
    <a class="btn btn-blue"><span class="icon-dot"></span>Get Involved</a>
    <a class="btn btn-orange"><span class="icon-dot"></span>Partnership</a>
    <a class="btn btn-yellow"><span class="icon-dot"></span>Donate Here</a>
  </div>
</section>

<section class="blog">
  <h2 class="section-title">Latest Blog Posts</h2>
  <div class="post-row" style="top:178px">
    <div class="ph" role="img" aria-label="Photo of a team of volunteers" style="background:linear-gradient(#a58c6e,#6a5a48)"></div>
    <div class="post-text"><h3>Moving as a Team</h3><p>Notes on how small groups grow stronger by serving side by side in our neighbourhoods.</p></div>
    <div class="mini-date">12<small>JUN</small></div>
  </div>
  <div class="post-row" style="top:290px">
    <div class="ph" role="img" aria-label="Photo of people gardening" style="background:linear-gradient(#8fa77a,#5d7450)"></div>
    <div class="post-text"><h3>What Are Our 5 Days With a Purpose Project?</h3><p>A look at five days of simple service that brought neighbours together across town.</p></div>
    <div class="mini-date">08<small>JUN</small></div>
  </div>
  <div class="post-row" style="top:402px">
    <div class="ph" role="img" aria-label="Photo of volunteers outdoors" style="background:linear-gradient(#9e9a6c,#6b6b49)"></div>
    <div class="post-text"><h3>Moving as a Team</h3><p>Stories from our latest serve day and the friends we made along the way this spring.</p></div>
    <div class="mini-date">02<small>JUN</small></div>
  </div>
  <article class="feature">
    <div class="ph" role="img" aria-label="Photo of neighbours planting a community garden" style="background:linear-gradient(120deg,#7e9a68,#a88f70 60%,#5d7450)"><div class="date-badge">23<small>JUN</small></div></div>
    <h3>10 Ways You Can Get Involved in Your Community</h3>
    <p>From mentoring students to sharing a meal, here are easy ways to love your neighbours well and make a real difference this season.</p>
  </article>
</section>

<section class="testimonials">
  <svg class="abs" style="inset:0" width="1200" height="482" viewBox="0 0 1200 482" preserveAspectRatio="none" role="img" aria-label="Faded photo of a community gathering, tinted blue">
    <path d="M0 60 C250 10 450 90 700 50 C900 20 1080 60 1200 30 L1200 482 L0 482 Z" fill="#5a88a0"/>
    <path d="M0 90 C300 40 500 120 760 80 C950 50 1100 90 1200 60 L1200 482 L0 482 Z" fill="#4c7991"/>
  </svg>
  <h2 class="section-title">Client Testimonials</h2>
  <div class="t-arrow" style="left:96px"><svg width="8" height="12"><path d="M7 1L2 6l5 5" stroke="#fff" stroke-width="2" fill="none"/></svg></div>
  <div class="t-arrow" style="right:96px"><svg width="8" height="12"><path d="M1 1l5 5-5 5" stroke="#fff" stroke-width="2" fill="none"/></svg></div>
  <div class="quote" style="left:172px"><span class="avatar" role="img" aria-label="Portrait of a volunteer"></span><p>Serving with this group changed how I see my own street. I know my neighbours by name now.</p><h4>Jordan Hale · Contractor</h4></div>
  <div class="quote" style="left:462px"><span class="avatar" role="img" aria-label="Portrait of a volunteer"></span><p>Every event feels welcoming and well planned. Our whole family looks forward to serve days.</p><h4>— Maya Ortiz</h4></div>
  <div class="quote" style="left:752px"><span class="avatar" role="img" aria-label="Portrait of a volunteer"></span><p>They showed up for our school when we needed help most. We are so thankful for them.</p><h4>Elena Brooks · Teacher</h4></div>
</section>

<section class="newsletter">
  <p>Join our mailing list and stay updated!</p>
  <div class="field" style="left:488px">Name</div>
  <div class="field" style="left:700px">Email Address</div>
  <a class="btn">Subscribe Now</a>
</section>

<section class="follow">
  <h2>Follow Us</h2>
  <div class="social">
    <span style="background:#3b5998"></span><span style="background:#29a9e0"></span><span style="background:#c13584"></span><span style="background:#d93a2b"></span><span style="background:#cb2027"></span>
  </div>
</section>

<div class="photo-strip">
  <span class="ph" role="img" aria-label="Photo of volunteers painting" style="background:linear-gradient(#a08a74,#6b5a4a)"></span>
  <span class="ph" role="img" aria-label="Photo of volunteers at work" style="background:linear-gradient(#b59b82,#7a6553)"></span>
  <span class="ph" role="img" aria-label="Photo of a volunteer repairing a home" style="background:linear-gradient(#8f9fa8,#5d6c75)"></span>
  <span class="ph" role="img" aria-label="Photo of friends laughing" style="background:linear-gradient(#c4a88e,#8a715c)"></span>
  <span class="ph" role="img" aria-label="Photo of a group serving food" style="background:linear-gradient(#a7968a,#6e6058)"></span>
  <span class="ph" role="img" aria-label="Photo of a work crew" style="background:linear-gradient(#9aa18c,#646a58)"></span>
</div>

<section class="contact">
  <h2>CONTACT US</h2>
  <div class="field" style="left:236px;top:108px;width:356px">First Name</div>
  <div class="field" style="left:608px;top:108px;width:356px">Last Name</div>
  <div class="field" style="left:236px;top:164px;width:728px">Email Address</div>
  <div class="field message" style="left:236px;top:220px;width:728px;height:150px">Message</div>
  <a class="btn btn-orange">Submit</a>
</section>

<footer class="site-footer">© KindAshbury.com · All rights reserved · #kindashbury</footer>

</body>
</html>
```